Special Educational Conference Poster

Looking for a poster that I can use electronically more than anything - to post on Chatterbook \ social media. Should be bold, eye catching, and within our brand colors.

3rd Annual Young Learners Beyond Limits Summit
Featuring Dr. Martin Ellery
Lighting the Way: Growing Courage, Drive, and Grit in Every Young Learner Who Thinks Differently

Friday, May 10, 2019, 9am - 3pm

The Linden Grove Academy at Fenwick opens our campus to teachers, parents, and practitioners from the Delaware Valley to learn together on how to support the extraordinary students in our lives. The conference runs from 9am - 3pm and lunch is included. This event is free and open to the public, but registration is required.

Link to registration: https://www.lindengroveacad.org/admissions/admissions-visit-and-events

```html
<!DOCTYPE html>
<html lang="en">
<head>
<meta charset="utf-8">
<title>Young Learners Beyond Limits Summit</title>
<link href="https://fonts.googleapis.com/css2?family=Oswald:wght@400;500;600&family=Roboto:wght@400;500&family=Tinos:wght@400;700&display=swap" rel="stylesheet">
<style>
  :root{
    --navy:#1f3a5c;
    --navy-deep:#172d48;
    --gold:#d6b534;
    --gold-soft:#e2c65a;
    --paper:#ffffff;
    --ink:#1c2230;
    --photo-light:#e9e8e6;
    --photo-mid:#cfcac6;
  }
  *{margin:0;padding:0;box-sizing:border-box}
  html,body{width:894px;height:1200px;overflow:hidden;background:#fff}
  .poster{position:relative;width:894px;height:1200px;background:var(--gold);overflow:hidden;font-family:"Tinos",serif;color:var(--ink)}
  .top-band{position:absolute;left:0;top:0;width:100%;height:20px;background:var(--navy)}
  .photo{position:absolute;left:0;top:20px;width:100%;height:490px;
    background:linear-gradient(180deg,var(--photo-light) 0%,var(--photo-mid) 60%,#b9b1ad 100%)}
  .sign{position:absolute;left:158px;top:232px;width:578px;height:290px;background:var(--paper);
    box-shadow:0 2px 6px rgba(0,0,0,.18);text-align:center;padding-top:78px}
  .sign .mark{display:inline-block;width:26px;height:26px;border-radius:50%;background:var(--navy);margin-bottom:10px}
  .sign .school{font-family:"Tinos",serif;font-weight:400;color:var(--navy);font-size:38px;line-height:1.08}
  .sign .rule{width:380px;height:3px;background:var(--gold);margin:10px auto 8px}
  .sign .tagline{font-family:"Tinos",serif;color:var(--navy);font-size:22px}
  .sign .url{font-family:"Tinos",serif;color:var(--ink);font-size:14px;margin-top:2px}
  .heading{position:absolute;top:540px;width:100%;text-align:center;font-family:"Oswald",sans-serif;text-transform:uppercase}
  .heading .kicker{font-size:32px;font-weight:500;color:var(--navy-deep);letter-spacing:.5px;line-height:1.1}
  .heading .title{font-size:60px;font-weight:600;color:var(--navy);line-height:1.05}
  .ribbon{position:absolute;top:664px;left:110px;width:674px;height:54px;display:flex;font-family:"Roboto",sans-serif;font-size:28px}
  .ribbon .day{width:180px;background:var(--navy);color:#fff;display:flex;align-items:center;justify-content:center;
    clip-path:polygon(0 0,100% 0,100% 100%,0 100%,18px 50%)}
  .ribbon .date{flex:1;background:#fff;color:var(--navy);display:flex;align-items:center;justify-content:center;font-weight:500}
  .ribbon .date sup{font-size:16px}
  .ribbon .time{width:200px;background:var(--navy);color:#fff;display:flex;align-items:center;justify-content:center;
    clip-path:polygon(0 0,100% 0,calc(100% - 18px) 50%,100% 100%,0 100%)}
  .intro{position:absolute;top:742px;left:100px;width:694px;font-size:19px;line-height:1.3;text-align:justify;color:var(--ink)}
  .lower{position:absolute;left:0;top:1068px;width:100%;height:102px;background:var(--paper)}
  .bottom-band{position:absolute;left:0;bottom:0;width:100%;height:30px;background:var(--navy)}
  .portrait{position:absolute;left:62px;top:918px;width:262px;height:262px;border-radius:50%;border:8px solid #fff;
    background:radial-gradient(circle at 50% 45%,#3d6ea8 0%,var(--navy) 100%);box-shadow:0 1px 4px rgba(0,0,0,.2)}
  .speaker{position:absolute;left:350px;top:935px;width:480px}
  .speaker .feature{font-family:"Roboto",sans-serif;font-size:25px;color:var(--navy)}
  .speaker .feature b{font-weight:500}
  .speaker .talk{font-size:18px;line-height:1.25;margin-top:4px}
  .touch{position:absolute;left:350px;top:1040px;width:210px;height:34px;border-radius:17px;background:var(--gold-soft);
    border:2px solid #fff;font-family:"Roboto",sans-serif;font-size:17px;color:var(--navy);padding-left:18px;line-height:30px}
  .contacts{position:absolute;left:352px;top:1084px;list-style:none;font-family:"Roboto",sans-serif;font-size:14px;color:var(--ink)}
  .contacts li{display:flex;align-items:center;height:26px}
  .contacts .dot{width:16px;height:16px;border-radius:50%;background:var(--navy);margin-right:8px;flex:none}
  .divider{position:absolute;left:654px;top:1042px;width:2px;height:120px;background:var(--navy)}
  .register{position:absolute;left:668px;top:1046px;width:200px;font-size:14px;line-height:1.3}
  .register .label{font-weight:700;font-size:17px;margin-bottom:4px}
  .register .link{word-break:break-all}
</style>
</head>
<body>
<div class="poster">
  <div class="top-band"></div>
  <div class="photo" role="img" aria-label="Photo of five smiling teenage students standing in front of a white brick wall, holding up the school sign"></div>

  <div class="sign">
    <span class="mark"></span>
    <div class="school">The Linden Grove Academy<br>at Fenwick</div>
    <div class="rule"></div>
    <div class="tagline">Where Childhood Shines</div>
    <div class="url">www.lindengroveacad.org</div>
  </div>

  <div class="heading">
    <div class="kicker">3rd Annual Young Learners</div>
    <div class="title">Beyond Limits Summit</div>
  </div>

  <div class="ribbon">
    <div class="day">Friday</div>
    <div class="date">10<sup>th</sup>&nbsp;May 2019</div>
    <div class="time">9am - 3pm</div>
  </div>

  <p class="intro">The Linden Grove Academy at Fenwick opens our campus to teachers, parents, and practitioners from the Delaware Valley to learn together on how to support the extraordinary students in our lives. The conference runs from 9am - 3pm and lunch is included. This event is free and open to the public, but registration is required.</p>

  <div class="lower"></div>
  <div class="bottom-band"></div>

  <div class="portrait" role="img" aria-label="Portrait photo of the featured speaker, Dr. Martin Ellery"></div>

  <div class="speaker">
    <div class="feature">Featuring <b>Dr. Martin Ellery</b></div>
    <p class="talk">Lighting the Way: Growing Courage, Drive, and Grit in Every Young Learner Who Thinks Differently</p>
  </div>

  <div class="touch">Get in touch:</div>
  <ul class="contacts">
    <li><span class="dot"></span>www.chatterbook.com/lindengroveacad</li>
    <li><span class="dot"></span>www.chirpline.com/lindengroveacad</li>
    <li><span class="dot"></span>www.snapgrid.com/lindengroveacad</li>
  </ul>

  <div class="divider"></div>
  <div class="register">
    <div class="label">Link to registration:</div>
    <div class="link">https://www.lindengroveacad.org/admissions/admissions-visit-and-events</div>
  </div>
</div>
</body>
</html>
```